VARLEX CONSULTING / PROJECT MANAGEMENT WEB DESIGN

Design Brief: Varlex Consulting Website

I own 'VARLEX' business name and therefore can keep the name and logo simple i.e. VARLEX only and incorporate consulting / Project Management within the design or text.

Purpose:

The purpose of this project is to create a website for Varlex.com.au, a project management consulting company. The website will promote the company's services, allowing potential clients to learn more about Varlex and its capabilities. The website should be professional, easy to navigate, and provide all necessary information for potential clients.

Target Audience:

Clients in the Oil & Gas, LNG, and Chemical industry
Businesses and organizations in need of project management and engineering consultancy services
Potential clients looking for information about the company and its services
Key Elements:
Clean and modern design that reflects the company's professional image and incorporates the company logo

Clear and easy-to-use navigation menu

“Homepage” that promotes the company's main services and includes the company's mission statement.

Services:

PROJECT MANAGEMENT
PROJECT ENGINEERING
QUALITY MANAGEMENT AND PROCESS DEVELOPMENT
BUSINESS CASE DEVELOPMENT
ENGINEERING & DESIGN MANAGEMENT
CONCEPT STUDIES AND PROJECT SUPPORT
CONSTRUCTION MANAGEMENT
CONTRACT MANAGEMENT / CLAIMS PROCUREMENT / SUPPLY CHAIN SUPPORT
COMMERCIAL LIABILITY & RISK MANAGEMENT

Mission Statement:

"Our mission at Varlex is to provide expert project management and engineering consultancy services that help our clients achieve their goals and exceed their expectations. We will accomplish this by offering a full range of services, providing experienced and highly-qualified professionals, building strong relationships with our clients, continuously improving our services, and maintaining a reputation for excellence."

"About" page that includes client-supplied text about the company
"Contact" page with an editable form, email, and phone number for potential clients to get in touch with the company

Design Style:

Professional and modern
Clean and simple layout
Use of the company's colors and branding (subject to change)
Use of high-quality images that reflect the industry and services

Functionality:
Responsive design that is optimized for all devices and screen sizes

Website will be coded and uploaded to a content management system (CMS) for easy updates and maintenance
Website will be optimized for search engines and include all necessary SEO elements
Website will be fully tested for compatibility with all modern web browsers and devices
Website will be secured with an SSL certificate to ensure the safety of user data (client hosting includes SSL certificate).

Target Market(s)

Clients in the Oil & Gas, LNG, and Chemical industry Businesses and organizations in need of project management and engineering consultancy services Potential clients looking for information about the company and its services

Industry/Entity Type

Oil & Gas, LNG, and Chemical industry Businesses and organizations

Coding

Coded - Design and coding required

Number of Pages Required

3 page

Font styles to use
Sans Serif

Colors
0054AA
0677BA
7BADD7
CADEEF
E8F1F8
EB3D1F
EC4F4E
F09395
F8D3D4
FCEDEE
6B429C
8869AF
B7A5CE
E3DAEB
F3F0F8

Requirements
Must have
• HOME ABOUT AND CONTACT PAGE
Nice to have
• Fresh look, open to ideas
Should not have
• Stock images and hand shakes and meeting rooms..

```html
<!DOCTYPE html>
<html lang="en">
<head>
<meta charset="utf-8">
<title>Varlex Consulting – Project Management &amp; Engineering Consultancy</title>
<link href="https://fonts.googleapis.com/css2?family=Montserrat:wght@400;500;600;700;800&display=swap" rel="stylesheet">
<style>
:root{
  --blue:#2aa8f5;
  --blue-deep:#1d96e6;
  --ink:#111111;
  --text:#3d3d3d;
  --white:#ffffff;
  --soft-bg:#f1f1f1;
  --hero-dark:#1f2226;
}
*{box-sizing:border-box;margin:0;padding:0}
html,body{width:1200px;height:3021px;overflow:hidden}
body{font-family:'Montserrat',sans-serif;color:var(--text);background:var(--white);position:relative}

/* Header */
.site-header{position:relative;height:102px;background:var(--white)}
.social{position:absolute;left:80px;top:49px;display:flex;gap:15px}
.social span{width:12px;height:12px;border-radius:50%;background:var(--ink);display:block}
.contact-email{position:absolute;left:226px;top:46px;font-size:13px;font-weight:500;color:var(--ink);display:flex;align-items:center;gap:8px}
.brand{position:absolute;left:50%;top:34px;transform:translateX(-50%);display:flex;align-items:center;gap:10px}
.brand-dot{width:30px;height:30px;border-radius:50%;background:var(--blue)}
.brand-name{font-size:34px;font-weight:700;color:var(--blue);letter-spacing:1px}
.main-nav{position:absolute;right:80px;top:47px;display:flex;gap:48px}
.main-nav a{font-size:13px;font-weight:700;color:var(--ink);text-decoration:none;letter-spacing:.5px}
.main-nav a.active{color:var(--blue);border-bottom:2px solid var(--blue);padding-bottom:4px}

/* Hero */
.hero{position:relative;height:538px;background:linear-gradient(120deg,#3a3b3d 0%,#24272b 40%,#2d2a26 70%,#6a5a43 100%);color:var(--white);text-align:center}
.hero-overlay{position:absolute;inset:0;background:rgba(20,22,26,.45)}
.hero-content{position:absolute;left:0;right:0;top:166px}
.hero h1{font-size:36px;font-weight:500;line-height:43px}
.hero h1 strong{color:var(--blue);font-weight:800}
.hero p{margin:44px auto 0;width:700px;font-size:16px;line-height:24px}
.btn{display:inline-flex;align-items:center;justify-content:center;gap:10px;background:var(--blue);color:var(--white);font-weight:600;font-size:14px;border-radius:30px;text-decoration:none;box-shadow:0 8px 18px rgba(42,168,245,.3)}
.hero .btn{position:absolute;left:507px;top:382px;width:182px;height:57px}

/* Section labels */
.eyebrow{font-size:15px;font-weight:700;color:var(--blue);letter-spacing:2px}
.section-title{font-size:38px;font-weight:800;color:var(--ink);line-height:43px}
.body-copy{font-size:14.5px;line-height:25.5px;color:var(--text)}

/* About */
.about{position:relative;height:639px}
.about .accent{position:absolute;left:143px;top:134px;width:230px;height:423px;background:var(--blue)}
.about .photo{position:absolute;left:171px;top:84px;width:359px;height:453px;background:linear-gradient(160deg,#d9d9d6,#8d8e8c 55%,#3f4450)}
.about .copy{position:absolute;left:605px;top:80px;width:465px}
.about .section-title{margin-top:16px}
.about .body-copy{margin-top:38px}
.about .btn{margin:38px 0 0 10px;width:183px;height:57px}

/* Services */
.services{position:relative;height:1082px;background:var(--soft-bg);text-align:center}
.services .eyebrow{padding-top:74px}
.services .section-title{margin-top:8px}
.service-grid{position:absolute;left:100px;top:173px;display:grid;grid-template-columns:repeat(3,317px);column-gap:25px;row-gap:25px;align-items:start}
.service-card{background:var(--white);min-height:248px;padding:28px 26px 30px}
.service-card svg{width:52px;height:52px;stroke:var(--blue);fill:none;stroke-width:1.6;stroke-linecap:round;stroke-linejoin:round}
.service-card h3{margin-top:20px;font-size:19px;font-weight:600;color:var(--ink);line-height:23px}
.service-card p{margin-top:22px;font-size:14px;line-height:17.5px;color:var(--text)}
.service-card h3.two-line + p{margin-top:6px}

/* Why */
.why{position:relative;height:660px}
.why .copy{position:absolute;left:128px;top:122px;width:470px}
.why .section-title{margin-top:18px}
.why .body-copy{margin-top:50px}
.why .btn{margin-top:38px;width:182px;height:56px}
.why .accent-top{position:absolute;left:960px;top:89px;width:152px;height:160px;background:var(--blue)}
.why .accent-bottom{position:absolute;left:701px;top:437px;width:153px;height:158px;background:var(--blue)}
.why .photo{position:absolute;left:730px;top:115px;width:359px;height:452px;background:linear-gradient(150deg,#e9e6df,#9a8d7c 45%,#1f2a3d 80%)}
</style>
</head>
<body>

<header class="site-header">
  <div class="social" aria-label="Social links"><span></span><span></span><span></span><span></span></div>
  <div class="contact-email">
    <svg width="14" height="11" viewBox="0 0 14 11"><rect x="0.5" y="0.5" width="13" height="10" rx="1" fill="#111"/><path d="M1 1l6 5 6-5" stroke="#fff" fill="none"/></svg>
    info@varlex.com.au
  </div>
  <div class="brand"><span class="brand-dot"></span><span class="brand-name">VARLEX</span></div>
  <nav class="main-nav">
    <a href="#" class="active">HOME</a>
    <a href="#">ABOUT</a>
    <a href="#">CONTACT US</a>
  </nav>
</header>

<section class="hero" role="img" aria-label="Team working together at a desk with laptops">
  <div class="hero-overlay"></div>
  <div class="hero-content">
    <h1><strong>WE</strong> provide expert PROJECT MANAGEMENT and<br>ENGINEERING <strong>CONSULTANCY.</strong></h1>
    <p>Lorem ipsum dolor sit amet, consectetur adipiscing elit. Etiam eu turpis molestie, dictum est a, mattis tellus. Sed dignissim, metus nec fringilla accumsan.</p>
  </div>
  <a href="#" class="btn">LEARN MORE</a>
</section>

<section class="about">
  <div class="accent"></div>
  <div class="photo" role="img" aria-label="Two colleagues reviewing a tablet together"></div>
  <div class="copy">
    <div class="eyebrow">ABOUT US</div>
    <h2 class="section-title">We help our clients<br>achieve their goals<br>and exceed</h2>
    <p class="body-copy">Lorem ipsum dolor sit amet, consectetur adipiscing elit. Etiam eu turpis molestie, dictum est a, mattis tellus. Sed dignissim, metus nec fringilla accumsan, risus sem sollicitudin lacus, ut interdum tellus elit sed risus. Maecenas eget condimentum velit, sit amet feugiat lectus. Class aptent taciti sociosqu ad litora torquent per conubia nostra, per inceptos himenaeos. Praesent auctor purus luctus enim egestas, ac scelerisque ante pulvinar.</p>
    <a href="#" class="btn">MORE ABOUT <svg width="7" height="10" viewBox="0 0 7 10"><path d="M1 0l6 5-6 5z" fill="#fff"/></svg></a>
  </div>
</section>

<section class="services">
  <div class="eyebrow">SERVICES</div>
  <h2 class="section-title">We Provide Best Service</h2>
  <div class="service-grid">
    <article class="service-card">
      <svg viewBox="0 0 52 52"><circle cx="30" cy="22" r="8"/><circle cx="30" cy="22" r="3"/><path d="M30 10v3M30 31v3M18 22h3M39 22h3M22 14l2 2M36 28l2 2M38 14l-2 2M22 30l2-2"/><path d="M20 42c-6-3-9-9-7-16"/><path d="M18 42h10v5H18z"/></svg>
      <h3>Project Management</h3>
      <p>Lorem ipsum dolor sit amet, consectetur adipiscing elit. Etiam eu turpis molestie.</p>
    </article>
    <article class="service-card">
      <svg viewBox="0 0 52 52"><circle cx="26" cy="26" r="18"/><circle cx="26" cy="26" r="11"/><path d="M15 26h22M26 15v22M19 19c4 3 10 3 14 0M19 33c4-3 10-3 14 0"/></svg>
      <h3>Project Engineering</h3>
      <p>Lorem ipsum dolor sit amet, consectetur adipiscing elit. Etiam eu turpis molestie.</p>
    </article>
    <article class="service-card">
      <svg viewBox="0 0 52 52"><circle cx="26" cy="26" r="19"/><circle cx="26" cy="26" r="11"/><path d="M21 26l4 4 7-8"/></svg>
      <h3 class="two-line">Quality Management And Process Development</h3>
      <p>Lorem ipsum dolor sit amet, consectetur adipiscing elit. Etiam eu turpis molestie.</p>
    </article>
    <article class="service-card">
      <svg viewBox="0 0 52 52"><path d="M8 44h36M12 36l10-10 7 6 15-16"/><path d="M36 14h9v9"/><circle cx="18" cy="40" r="3"/></svg>
      <h3 class="two-line"><b>Business Case Development</b></h3>
      <p>Lorem ipsum dolor sit amet, consectetur adipiscing elit. Etiam eu turpis molestie.</p>
    </article>
    <article class="service-card">
      <svg viewBox="0 0 52 52"><circle cx="24" cy="26" r="14"/><circle cx="24" cy="26" r="6"/><path d="M32 20h12M32 26h14M32 32h12"/></svg>
      <h3 class="two-line">Engineering &amp; Design Management</h3>
      <p>Lorem ipsum dolor sit amet, consectetur adipiscing elit. Etiam eu turpis molestie.</p>
    </article>
    <article class="service-card">
      <svg viewBox="0 0 52 52"><circle cx="26" cy="26" r="17"/><path d="M18 34l16-16M34 34L18 18"/><circle cx="26" cy="26" r="4"/></svg>
      <h3 class="two-line">Concept Studies And Project Support</h3>
      <p>Lorem ipsum dolor sit amet, consectetur adipiscing elit. Etiam eu turpis molestie.</p>
    </article>
    <article class="service-card">
      <svg viewBox="0 0 52 52"><circle cx="26" cy="26" r="18"/><path d="M15 38V24h8v14M23 38V16h9v22M32 38V28h6v10M12 40h28"/></svg>
      <h3>Construction Management</h3>
      <p>Lorem ipsum dolor sit amet, consectetur adipiscing elit. Etiam eu turpis molestie.</p>
    </article>
    <article class="service-card">
      <svg viewBox="0 0 52 52"><rect x="16" y="10" width="20" height="30" rx="2"/><path d="M20 28h12M20 33h12"/><rect x="22" y="16" width="8" height="7"/><circle cx="42" cy="16" r="2"/><circle cx="44" cy="28" r="2"/><circle cx="42" cy="40" r="2"/><path d="M12 18c-5 5-5 11 0 16"/></svg>
      <h3 class="two-line">Contract Management / Claims Procurement / Supply Chain Support</h3>
      <p>Lorem ipsum dolor sit amet, consectetur adipiscing elit. Etiam eu turpis molestie.</p>
    </article>
    <article class="service-card">
      <svg viewBox="0 0 52 52"><path d="M26 8l16 34H10z"/><path d="M26 20v11M26 35v2"/><path d="M20 6h12"/></svg>
      <h3 class="two-line">Commercial Liability &amp; Risk Management</h3>
      <p>Lorem ipsum dolor sit amet, consectetur adipiscing elit. Etiam eu turpis molestie.</p>
    </article>
  </div>
</section>

<section class="why">
  <div class="copy">
    <div class="eyebrow">WHY US</div>
    <h2 class="section-title">We help you lorem<br>ipsum dolor</h2>
    <p class="body-copy">Lorem ipsum dolor sit amet, consectetur adipiscing elit. Etiam eu turpis molestie, dictum est a, mattis tellus. Sed dignissim, metus nec fringilla accumsan, risus sem sollicitudin lacus, ut interdum tellus elit sed risus. Maecenas eget condimentum velit, sit amet feugiat lectus. Class aptent taciti sociosqu ad litora torquent per conubia nostra, per inceptos himenaeos. Praesent auctor purus luctus enim egestas, ac scelerisque ante pulvinar.</p>
    <a href="#" class="btn">MORE ABOUT <svg width="7" height="10" viewBox="0 0 7 10"><path d="M1 0l6 5-6 5z" fill="#fff"/></svg></a>
  </div>
  <div class="accent-top"></div>
  <div class="accent-bottom"></div>
  <div class="photo" role="img" aria-label="Consultant in a suit working on a tablet with a colleague"></div>
</section>

</body>
</html>
```